REDESIGN SIGN UP PAGE - EASY TO READ AND UNDERSTAND QUICKLY

I need to redesign my sign up page DESKTOP AND MOBILE VERSION to include 2 products that are each available as a monthly subscription, 6 mth or 12 mth subscription.

Currently I only promote one product on my website but now will be two. https://www.brightlanerewardhub.biz/signup

Now I will have two products:

1. UNLIMITED VACATION CERTIFICATES, DINING VOUCHERS & SAVINGS INCENTIVES
Unlimited Monthly Plan $99 / Month + $199 One-Time Set-Up Fee
Unlimited Bi Annual Plan $490 / 6 Months + $199 One-Time Set-Up Fee
Unlimited Annual Plan $898 / 12 Months + $199 One-Time Set-Up Fee

2. UNLIMITED SMART DEVICE INCENTIVES & OTHER HARD PREMIUMS
Unlimited Monthly Plan $299 / Month + $199 One-Time Set-Up Fee
Unlimited Bi Annual Plan $1,590 / 6 Months + $199 One-Time Set-Up Fee
Unlimited Annual Plan $2,898 / 12 Months + $199 One-Time Set-Up Fee

When promoting the different plans you can see the different categories of incentives I offer here: https://www.brightlanerewardhub.biz/incentives

The SMART DEVICE CERTIFICATES & INCENTIVES category is for product #2 and all the rest of the Categories is for Product #1 Feel free to use images as a visual so customers can see that this product includes Vacations & Restaurants and this product includes only smart devices....

USE ALL CURRENT BULLET POINTS FOR BOTH PLANS THAT IS CURRENTLY ON WEBSITE. USE ALL CURRENT CONTENT ON WEBSITE ORIGINAL SIGN UP PAGE. DO NOT LEAVE ANY CONTENT OUT.

Target Market(s)

BUSINESS OWNERS

Industry/Entity Type

Marketing

Number of Pages Required

2 page

Requirements
Must have
• When promoting the 2 different products on the new sign up page you can see the different categories of incentives I offer here: https://www.brightlanerewardhub.biz/incentives fee; free to use images to showcase what each product offers.

The SMART DEVICE CERTIFICATES & INCENTIVES category is for product #2 and all the rest of the Categories is for Product #1

I want the user to easily understand we have two products that are available in 3 ways, monthly subscription, bi annual and annual and can see the price immediately for all 3 options for both products without toggling, etc.

Must be super clean easy to ready design. Not too busy at all please
Nice to have
• USE ALL CURRENT BULLET POINTS FOR BOTH PLANS THAT IS CURRENTLY ON WEBSITE. USE ALL CURRENT CONTENT ON WEBSITE ORIGINAL SIGN UP PAGE. DO NOT LEAVE ANY CONTENT OUT.

Should not have

```html
<!DOCTYPE html>
<html lang="en">
<head>
<meta charset="utf-8">
<title>Sign Up – Brightlane Reward Hub</title>
<link href="https://fonts.googleapis.com/css2?family=Poppins:wght@300;400;500;600;700&display=swap" rel="stylesheet">
<style>
:root{
  --blue:#1a82e2;
  --nav-blue:#1877cc;
  --btn-blue:#0a7cf0;
  --ink:#2b2b2b;
  --muted:#9a9a9a;
  --line:#d7d7d7;
  --head-grey:#5b6066;
  --green:#4caf50;
  --footer:#172532;
  --footer-text:#aab3bd;
}
*{margin:0;padding:0;box-sizing:border-box}
html,body{width:815px;height:1200px;overflow:hidden;background:#fff}
body{position:relative;font-family:"Poppins",sans-serif;color:var(--ink)}
.abs{position:absolute}

/* header */
.topbar{left:0;top:0;width:815px;height:29px}
.brand{left:16px;top:7px;display:flex;align-items:center;gap:5px}
.brand-mark{width:14px;height:14px;background:var(--blue)}
.brand-name{font-size:9px;font-weight:600;color:var(--blue);line-height:1}
.nav{left:200px;top:0;height:29px;display:flex;align-items:center;gap:9px;font-size:5px;font-weight:700;color:#fff}
.account{top:0;height:29px;width:34px;display:flex;flex-direction:column;align-items:center;justify-content:center;font-size:5px;color:#fff;gap:2px}
.account.login{left:654px;background:#4a4e54}
.account.signup{left:688px;background:var(--nav-blue)}
.callbox{left:722px;top:0;width:93px;height:29px;background:var(--green);display:flex;align-items:center;gap:5px;padding-left:7px;color:#fff;font-size:4.3px;font-weight:700;line-height:1.5}

/* intro */
.intro{left:0;top:64px;width:815px;text-align:center}
.intro h1{font-size:22px;font-weight:500;line-height:24px;color:#2b2b2b}
.intro h1 span{display:block;color:var(--blue)}
.intro p{margin:6px auto 0;width:330px;font-size:8px;line-height:11.5px}

/* pricing */
.product{left:111px;width:586px;height:216px}
.product-label{position:absolute;left:0;top:41px;width:234px;height:167px;border:1px solid var(--line)}
.product-label .name{position:absolute;left:0;top:0;width:100%;height:86px;display:flex;align-items:center;justify-content:flex-end;text-align:right;padding-right:18px;font-size:10.5px;font-weight:600;line-height:12.5px}
.product-label .fee{position:absolute;left:0;top:86px;width:100%;height:37px;border-top:1px solid var(--line);border-bottom:1px solid var(--line);display:flex;align-items:center;justify-content:center;color:var(--blue);font-weight:600;font-size:10.5px}
.plan{position:absolute;top:0;width:110px;height:208px;border:1px solid var(--line)}
.plan-head{height:41px;background:var(--head-grey);color:#fff;text-align:center;font-weight:600;font-size:13px;line-height:15px;padding-top:6px;margin:-1px -1px 0}
.plan-price{height:86px;border-bottom:1px solid var(--line);text-align:center}
.plan-price .amt{font-size:30px;font-weight:300;line-height:30px;padding-top:24px}
.plan-price .per{font-size:6px;color:var(--muted);margin-top:9px}
.plan-check{height:37px;border-bottom:1px solid var(--line);display:flex;align-items:center;justify-content:center}
.plan-select{height:44px;display:flex;align-items:center;justify-content:center}
.select-btn{width:90px;height:23px;background:var(--btn-blue);color:#fff;font-size:8px;font-weight:500;display:flex;align-items:center;justify-content:center}

/* includes */
.includes-title{left:0;top:680px;width:815px;text-align:center;font-size:21px;font-weight:400}
.features{left:128px;top:758px;width:580px;display:grid;grid-template-columns:194px 195px 191px;grid-auto-rows:30.2px;font-size:8px;line-height:11.5px}
.feature{display:flex;gap:9px;align-items:flex-start}
.feature svg{flex:none;margin-top:2px}

/* footer */
.footer{left:0;top:1013px;width:815px;height:187px;background:var(--footer);color:var(--footer-text);font-size:4.6px;line-height:7px}
.footer-brand{left:193px;top:30px;width:100px;display:flex;flex-direction:column;align-items:center;gap:4px}
.footer-brand .brand-name{font-size:8px;color:var(--blue);text-align:center}
.footer-brand .brand-mark{width:10px;height:10px}
.socials{left:206px;top:64px;display:flex;gap:3px}
.socials span{width:16px;height:16px;border-radius:50%;background:#5d6670;display:block}
.samples-btn{left:194px;top:90px;width:97px;height:22px;background:var(--green);color:#fff;text-align:center;font-weight:700;font-size:5.5px;line-height:7px;padding-top:4px}
.samples-btn small{display:block;font-size:4.3px;font-weight:500}
.footer h4{font-size:6.5px;font-weight:700;color:#fff;margin-bottom:8px;letter-spacing:.2px}
.col-contact{left:312px;top:26px;width:130px}
.col-quick{left:449px;top:26px;width:75px}
.col-other{left:531px;top:26px;width:95px}
.footer ul{list-style:none}
.footer li{margin-bottom:3px}
.contact-row{display:flex;gap:4px;margin-bottom:4px}
.contact-row b{color:#fff}
.hl{color:var(--green)}
.divider{position:absolute;top:24px;width:1px;height:140px;background:#2b3947}
.legal{left:193px;top:175px;width:430px;display:flex;justify-content:space-between;font-size:4.6px}
.legal b{color:#fff}
.chat{left:781px;top:1174px;width:20px;height:20px;border-radius:50%;background:#e8302a;display:flex;align-items:center;justify-content:center}
</style>
</head>
<body>

<header class="abs topbar">
  <svg class="abs" style="left:0;top:0" width="815" height="29"><polygon points="176,0 815,0 815,29 184,29 190,14" fill="var(--nav-blue)"/></svg>
  <div class="abs brand"><span class="brand-mark"></span><span class="brand-name">Brightlane Reward Hub</span></div>
  <nav class="abs nav"><span>Home</span><span>The Incentives</span><span>Samples</span><span>Industries</span><span>Testimonials</span><span>Faq</span><span>Integrations</span></nav>
  <div class="abs account login"><svg width="7" height="7" viewBox="0 0 10 10"><circle cx="5" cy="3" r="2.4" fill="#fff"/><path d="M1 10c0-3 2-4.5 4-4.5s4 1.5 4 4.5z" fill="#fff"/></svg>LOGIN</div>
  <div class="abs account signup"><svg width="7" height="7" viewBox="0 0 10 10"><circle cx="5" cy="5" r="4.3" fill="none" stroke="#fff"/><path d="M5 7.5V3M3 5l2-2 2 2" stroke="#fff" fill="none"/></svg>SIGN UP</div>
  <div class="abs callbox"><svg width="7" height="11" viewBox="0 0 7 11"><rect x=".6" y=".6" width="5.8" height="9.8" rx="1" fill="none" stroke="#fff" stroke-width="1.1"/></svg><div>CALL US: 1-555-014-2290<br>TEXT US: 1-555-014-7731</div></div>
</header>

<section class="abs intro">
  <h1>Congratulations on making the decision<span>to make more money for your business</span></h1>
  <p>This program is an online subscription based incentive marketing system with the following features</p>
</section>

<!-- product 1 -->
<section class="abs product" style="top:186px">
  <div class="product-label">
    <div class="name">Unlimited Vacation Certificates, Dining<br>Vouchers &amp; Savings Incentives</div>
    <div class="fee">$199 One-Time Set-Up Fee</div>
  </div>
  <div class="plan" style="left:241px"><div class="plan-head">Unlimited<br>Monthly Plan</div><div class="plan-price"><div class="amt">$99</div><div class="per">per month</div></div><div class="plan-check"><svg width="9" height="7" viewBox="0 0 9 7"><path d="M1 3.5l2.5 2.5L8 1" fill="none" stroke="var(--btn-blue)" stroke-width="1.6"/></svg></div><div class="plan-select"><div class="select-btn">Select</div></div></div>
  <div class="plan" style="left:358px"><div class="plan-head">Unlimited<br>Bi Annual Plan</div><div class="plan-price"><div class="amt">$490</div><div class="per">6 months</div></div><div class="plan-check"><svg width="9" height="7" viewBox="0 0 9 7"><path d="M1 3.5l2.5 2.5L8 1" fill="none" stroke="var(--btn-blue)" stroke-width="1.6"/></svg></div><div class="plan-select"><div class="select-btn">Select</div></div></div>
  <div class="plan" style="left:476px"><div class="plan-head">Unlimited<br>Annual Plan</div><div class="plan-price"><div class="amt">$898</div><div class="per">12 months</div></div><div class="plan-check"><svg width="9" height="7" viewBox="0 0 9 7"><path d="M1 3.5l2.5 2.5L8 1" fill="none" stroke="var(--btn-blue)" stroke-width="1.6"/></svg></div><div class="plan-select"><div class="select-btn">Select</div></div></div>
</section>

<!-- product 2 -->
<section class="abs product" style="top:426px">
  <div class="product-label">
    <div class="name">Unlimited Smart Device Incentives &amp;<br>Other Hard Premiums</div>
    <div class="fee">$199 One-Time Set-Up Fee</div>
  </div>
  <div class="plan" style="left:241px"><div class="plan-head">Unlimited<br>Monthly Plan</div><div class="plan-price"><div class="amt">$299</div><div class="per">per month</div></div><div class="plan-check"><svg width="9" height="7" viewBox="0 0 9 7"><path d="M1 3.5l2.5 2.5L8 1" fill="none" stroke="var(--btn-blue)" stroke-width="1.6"/></svg></div><div class="plan-select"><div class="select-btn">Select</div></div></div>
  <div class="plan" style="left:358px"><div class="plan-head">Unlimited<br>Bi Annual Plan</div><div class="plan-price"><div class="amt">$1,590</div><div class="per">6 months</div></div><div class="plan-check"><svg width="9" height="7" viewBox="0 0 9 7"><path d="M1 3.5l2.5 2.5L8 1" fill="none" stroke="var(--btn-blue)" stroke-width="1.6"/></svg></div><div class="plan-select"><div class="select-btn">Select</div></div></div>
  <div class="plan" style="left:476px"><div class="plan-head">Unlimited<br>Annual Plan</div><div class="plan-price"><div class="amt">$2,898</div><div class="per">12 months</div></div><div class="plan-check"><svg width="9" height="7" viewBox="0 0 9 7"><path d="M1 3.5l2.5 2.5L8 1" fill="none" stroke="var(--btn-blue)" stroke-width="1.6"/></svg></div><div class="plan-select"><div class="select-btn">Select</div></div></div>
</section>

<h2 class="abs includes-title">Every plan includes</h2>

<ul class="abs features" style="list-style:none">
  <li class="feature"><svg width="9" height="7" viewBox="0 0 9 7"><path d="M1 3.5l2.5 2.5L8 1" fill="none" stroke="var(--btn-blue)" stroke-width="1.6"/></svg>Unlimited Certificate Types</li>
  <li class="feature"><svg width="9" height="7" viewBox="0 0 9 7"><path d="M1 3.5l2.5 2.5L8 1" fill="none" stroke="var(--btn-blue)" stroke-width="1.6"/></svg>Unlimited E-Certificates</li>
  <li class="feature"><svg width="9" height="7" viewBox="0 0 9 7"><path d="M1 3.5l2.5 2.5L8 1" fill="none" stroke="var(--btn-blue)" stroke-width="1.6"/></svg>Unlimited SMS Certificates</li>
  <li class="feature"><svg width="9" height="7" viewBox="0 0 9 7"><path d="M1 3.5l2.5 2.5L8 1" fill="none" stroke="var(--btn-blue)" stroke-width="1.6"/></svg>Unlimited Web Banner Certificates</li>
  <li class="feature"><svg width="9" height="7" viewBox="0 0 9 7"><path d="M1 3.5l2.5 2.5L8 1" fill="none" stroke="var(--btn-blue)" stroke-width="1.6"/></svg>Unlimited White Label Certiifcate Landing Pages</li>
  <li class="feature"><svg width="9" height="7" viewBox="0 0 9 7"><path d="M1 3.5l2.5 2.5L8 1" fill="none" stroke="var(--btn-blue)" stroke-width="1.6"/></svg>Unlimited Website Sticky Bar Certificates</li>
  <li class="feature"><svg width="9" height="7" viewBox="0 0 9 7"><path d="M1 3.5l2.5 2.5L8 1" fill="none" stroke="var(--btn-blue)" stroke-width="1.6"/></svg>Unlimited Website Pop Up Certificate</li>
  <li class="feature"><svg width="9" height="7" viewBox="0 0 9 7"><path d="M1 3.5l2.5 2.5L8 1" fill="none" stroke="var(--btn-blue)" stroke-width="1.6"/></svg>Unlimited API E-Certificates</li>
  <li class="feature"><svg width="9" height="7" viewBox="0 0 9 7"><path d="M1 3.5l2.5 2.5L8 1" fill="none" stroke="var(--btn-blue)" stroke-width="1.6"/></svg>Unlimited Linkflow Integration Access</li>
  <li class="feature"><svg width="9" height="7" viewBox="0 0 9 7"><path d="M1 3.5l2.5 2.5L8 1" fill="none" stroke="var(--btn-blue)" stroke-width="1.6"/></svg>FREE Warm Lead Letter Templates</li>
  <li class="feature"><svg width="9" height="7" viewBox="0 0 9 7"><path d="M1 3.5l2.5 2.5L8 1" fill="none" stroke="var(--btn-blue)" stroke-width="1.6"/></svg>FREE Customer Appreciation Letter Templates</li>
  <li class="feature"><svg width="9" height="7" viewBox="0 0 9 7"><path d="M1 3.5l2.5 2.5L8 1" fill="none" stroke="var(--btn-blue)" stroke-width="1.6"/></svg>FREE Professional-Grade Incentive Videos</li>
  <li class="feature"><svg width="9" height="7" viewBox="0 0 9 7"><path d="M1 3.5l2.5 2.5L8 1" fill="none" stroke="var(--btn-blue)" stroke-width="1.6"/></svg>FREE Proven SocialFeed Ad Templates</li>
  <li class="feature"><svg width="9" height="7" viewBox="0 0 9 7"><path d="M1 3.5l2.5 2.5L8 1" fill="none" stroke="var(--btn-blue)" stroke-width="1.6"/></svg>FREE High-Converting Banner Ad Templates</li>
  <li class="feature"><svg width="9" height="7" viewBox="0 0 9 7"><path d="M1 3.5l2.5 2.5L8 1" fill="none" stroke="var(--btn-blue)" stroke-width="1.6"/></svg>FREE Time-Tested Print Ad Templates</li>
  <li class="feature"><svg width="9" height="7" viewBox="0 0 9 7"><path d="M1 3.5l2.5 2.5L8 1" fill="none" stroke="var(--btn-blue)" stroke-width="1.6"/></svg>FREE White Label Redemption Website</li>
  <li class="feature"><svg width="9" height="7" viewBox="0 0 9 7"><path d="M1 3.5l2.5 2.5L8 1" fill="none" stroke="var(--btn-blue)" stroke-width="1.6"/></svg>FREE Industry Specific Ad Packs</li>
  <li class="feature"><svg width="9" height="7" viewBox="0 0 9 7"><path d="M1 3.5l2.5 2.5L8 1" fill="none" stroke="var(--btn-blue)" stroke-width="1.6"/></svg>FREE Affiliate Program-Earn 50% Commissions</li>
  <li class="feature"><svg width="9" height="7" viewBox="0 0 9 7"><path d="M1 3.5l2.5 2.5L8 1" fill="none" stroke="var(--btn-blue)" stroke-width="1.6"/></svg>FREE Eye-Catching Posters, Flyers &amp; Brochures Each Certificate</li>
  <li class="feature"><svg width="9" height="7" viewBox="0 0 9 7"><path d="M1 3.5l2.5 2.5L8 1" fill="none" stroke="var(--btn-blue)" stroke-width="1.6"/></svg>FREE Step by Step Redemption Guides</li>
</ul>

<footer class="abs footer">
  <div class="abs footer-brand"><span class="brand-mark"></span><span class="brand-name">Brightlane Reward Hub</span></div>
  <div class="abs socials"><span></span><span></span><span></span><span></span></div>
  <div class="abs samples-btn">GET FREE SAMPLES<small>100% FREE</small></div>
  <span class="divider" style="left:303px"></span>
  <div class="abs col-contact">
    <h4>CONTACT US</h4>
    <div class="contact-row"><svg width="5" height="6" viewBox="0 0 10 12"><path d="M5 11.5S1 7 1 4.5a4 4 0 018 0C9 7 5 11.5 5 11.5z" fill="none" stroke="currentColor"/></svg><div><b>Brightlane Reward Group, Inc.</b><br>418 Harbor Crest Way Suite 120<br>Lakeview, CA 90000</div></div>
    <div class="contact-row"><svg width="5" height="5" viewBox="0 0 10 10"><path d="M2 1l2 2-1 1.5c1 1.5 2 2.5 3.5 3.5L8 7l2 2-1.5 1C4 9.5.5 6 0 1.5z" fill="none" stroke="currentColor" stroke-width=".8"/></svg><div>USA Office: <b>1-555-014-2290</b><br>International: <b>1-800-555-0148</b><br>Text Us: <b>1-555-014-3306</b></div></div>
    <div class="contact-row"><svg width="6" height="5" viewBox="0 0 12 9"><rect x=".5" y=".5" width="11" height="8" fill="none" stroke="currentColor"/><path d="M.5.5l5.5 4 5.5-4" fill="none" stroke="currentColor"/></svg><div>hello@brightlanerewardhub.biz</div></div>
    <div class="contact-row"><svg width="5" height="5" viewBox="0 0 10 10"><circle cx="5" cy="5" r="4.3" fill="none" stroke="currentColor"/><path d="M5 2.5V5h2" fill="none" stroke="currentColor"/></svg><div>24/7 Chat Support<br>24/7 Live Answering Service<br>24/7 Email Support<br><span class="hl">Live Phone &amp; SMS Support:</span><br>Monday - Friday 8am - 5pm PST<br><span class="hl">Sat/Sun/Holidays Closed</span></div></div>
  </div>
  <span class="divider" style="left:440px"></span>
  <div class="abs col-quick">
    <h4>QUICK LINKS</h4>
    <ul><li>Home</li><li>The Incentives</li><li>Samples</li><li>Affiliate</li><li>Testimonials</li><li>Faq</li><li>Contact Us</li><li>Redemption Demo Videos</li><li>BRH Distribute Certificate Demo Videos</li></ul>
  </div>
  <span class="divider" style="left:521px"></span>
  <div class="abs col-other">
    <h4>OTHER LINKS</h4>
    <ul><li>Hoteliers</li><li>BRH Certificates List</li><li>How To Use BRH Certificates</li><li>SocialFeed Incentive Campaign</li><li>Pop Ups &amp; Sticky Bars</li><li>Whitepaper - Increase Sales</li><li>Whitepaper - Improve Sales During Strange Times</li><li>Whitepaper - Boost Website Conversions</li></ul>
  </div>
  <div class="abs legal"><span>© 2020 <b>Brightlane Reward Group, Inc.</b> All Rights Reserved. CST# 0000000 <span style="color:var(--blue)">TCRC#</span> 000000</span><span>Privacy Policy &nbsp;|&nbsp; Term And Conditions</span></div>
</footer>
<div class="abs chat"><svg width="9" height="9" viewBox="0 0 10 10"><rect x="1" y="1" width="8" height="7" rx="1.5" fill="#fff"/><path d="M3 5.5c1 .8 3 .8 4 0" stroke="#e8302a" fill="none" stroke-width=".8"/></svg></div>

</body>
</html>
```